Wine label for family vineyard start-up

Brand new family vineyard needs a new label:

The information we need on the label is the following:
- Merlot & Cabernet (variety)
- Ponte Capriasca (location)
- 2016 (vintage)

The style of the label should be graphic / minimal / masculine.

This is a wine made by three 35yr old guys

Target Market(s)

young & urban

Industry/Entity Type

Vineyard

Logo Text

Merlot & Cabernet / Ponte Capriasca / 2016

Font styles to use
Sans Serif

Requirements
Must have
• clearly legible
• aesthetically pleasing [minimalist]
• sans serif

```html
<!DOCTYPE html>
<html lang="en">
<head>
<meta charset="utf-8">
<title>Merlot &amp; Cabernet – Ponte Capriasca 2016 wine label</title>
<link rel="stylesheet" href="https://fonts.googleapis.com/css2?family=Tenor+Sans&display=swap">
<style>
  :root {
    --page-bg: #ffffff;
    --label-center: #fffdf1;
    --label-edge: #e6e0c9;
    --label-rim: #d8d1b8;
    --ink: #1c1a17;
    --bloom: #c0187f;
    --leaf: #8cc63f;
  }
  * { margin: 0; padding: 0; box-sizing: border-box; }
  html, body {
    width: 1104px;
    height: 1200px;
    overflow: hidden;
    background: var(--page-bg);
  }
  .canvas {
    position: relative;
    width: 1104px;
    height: 1200px;
  }
  .wine-label {
    position: absolute;
    left: 202px;
    top: 82px;
    width: 700px;
    height: 1036px;
    background: radial-gradient(ellipse at 50% 48%, var(--label-center) 0%, #fbf7e6 45%, var(--label-edge) 100%);
    border-top: 2px solid var(--label-rim);
    border-bottom: 2px solid var(--label-rim);
    color: var(--ink);
    font-family: "Tenor Sans", "Helvetica Neue", Arial, sans-serif;
    font-weight: 400;
    font-variant-caps: small-caps;
  }
  .variety,
  .origin,
  .vintage {
    position: absolute;
    left: 0;
    width: 100%;
    text-align: center;
    font-weight: 400;
    line-height: 1.2;
    white-space: nowrap;
  }
  .variety {
    top: 112px;
    font-size: 48px;
  }
  .flower-branch {
    position: absolute;
    left: 60px;
    top: 228px;
    width: 580px;
    height: 528px;
  }
  .origin {
    top: 772px;
    font-size: 48px;
  }
  .vintage {
    top: 840px;
    font-size: 42px;
  }
  .label-footer {
    position: absolute;
    top: 980px;
    left: 22px;
    right: 22px;
    display: flex;
    justify-content: space-between;
    font-size: 20px;
    line-height: 1;
  }
</style>
</head>
<body>
  <main class="canvas">
    <section class="wine-label">
      <h1 class="variety">Merlot &amp; Cabernet</h1>
      <svg class="flower-branch" viewBox="0 0 580 528" role="img" aria-label="Illustration of a magenta flower on a curving stem with three patterned green leaves">
        <defs>
          <linearGradient id="branch-tones" x1="0" y1="0.3" x2="1" y2="0.7">
            <stop offset="0" stop-color="#c0187f" stop-opacity="0.5"/>
            <stop offset="0.45" stop-color="#b9689a" stop-opacity="0.25"/>
            <stop offset="1" stop-color="#8cc63f" stop-opacity="0.45"/>
          </linearGradient>
        </defs>
        <rect x="0" y="0" width="580" height="528" rx="40" fill="url(#branch-tones)"/>
      </svg>
      <h2 class="origin">Ponte Capriasca</h2>
      <p class="vintage">2016</p>
      <footer class="label-footer">
        <span class="volume">0,75 L</span>
        <span class="alcohol">7% alc. vol.</span>
      </footer>
    </section>
  </main>
</body>
</html>
```